Magician | Speaker looks for an innovative business card design

I'm a magician and public speaker offering artistic and modern magical experiences.
I'm based in Brussels (Belgium.) I love magic performed up-close, creating a space of intimacy, even when I'm on stage.
The final design should communicate professionalism, elegance, artistry, and a friendly kind personality

I would like to see designs based either on my photos and/or the way I sign my name Remy Vok (see attached files for more info.)
Additional photos and more info about what I offer can be seen at www.remy-vok.net

My current business card design is also attached. I like the fact that the reverse of my current design includes quotes from master magicians about magic, changing the way my participants see the art of magic.

Note: I would like a double-sided card design. However, I need white space on the reverse to be able to write things on for my performances.

Details to include on the card:
Artist name: Remy Vok
Offer: magician + (public) speaker or magic + (public) speaking (the + sign can be replaced by another character, like a bullet or a pipe)
Phone: +32 471 265 903
Email: book@remy-vok.net
(optional) Website: www.remy-vok.net or remy-vok.net

Target Market(s)

Corporate, organisations, companies as well as individuals

Industry/Entity Type

Artists

Colors

Designer to choose colors to be used in the design.

Requirements
Nice to have
• A side with a mirror could be nice

```html
<!DOCTYPE html>
<html lang="en">
<head>
<meta charset="utf-8">
<title>Remy Vok – Business Card</title>
<link rel="stylesheet" href="https://fonts.googleapis.com/css2?family=Cinzel:wght@400&family=Questrial&display=swap">
<style>
  :root {
    --page-bg: #ffffff;
    --card-bg: #141211;
    --ink-light: #ffffff;
    --ink-muted: #9a9a9a;
  }
  html, body {
    margin: 0;
    padding: 0;
    width: 1200px;
    height: 1200px;
    overflow: hidden;
    background: var(--page-bg);
  }
  .canvas {
    position: relative;
    width: 1200px;
    height: 1200px;
  }
  .card {
    position: absolute;
    left: 76px;
    top: 325px;
    width: 1048px;
    height: 550px;
    background: var(--card-bg);
    color: var(--ink-light);
    font-family: "Questrial", "Century Gothic", sans-serif;
  }
  .card__brand {
    position: absolute;
    left: 276px;
    top: 168px;
    margin: 0;
    font-family: "Cinzel", "Trajan Pro", serif;
    font-weight: 400;
    font-size: 112px;
    line-height: 1;
    letter-spacing: 2px;
    color: var(--ink-light);
  }
  .card__offer {
    position: absolute;
    left: 278px;
    top: 318px;
    margin: 0;
    font-size: 31px;
    letter-spacing: 0.5px;
  }
  .card__phone {
    position: absolute;
    left: 27px;
    top: 486px;
    font-size: 34px;
  }
  .card__web {
    position: absolute;
    right: 30px;
    top: 448px;
    font-size: 19px;
    letter-spacing: 4px;
    color: var(--ink-muted);
    text-transform: uppercase;
  }
  .card__email {
    position: absolute;
    right: 30px;
    top: 486px;
    font-size: 34px;
  }
</style>
</head>
<body>
  <main class="canvas">
    <section class="card" aria-label="Business card front">
      <h1 class="card__brand">Remy Vok</h1>
      <p class="card__offer">magician - (public) speaker</p>
      <span class="card__web">www.remy-vok.net</span>
      <span class="card__phone">+32 471 265 903</span>
      <span class="card__email">book@remy-vok.net</span>
    </section>
  </main>
</body>
</html>
```